Hörbuchcover
Zielgruppe
Spiritueller Hörbuchverlag für ganzheitliche Gesundheit, Glück und Wohlstand.
Aufgabenstellung
Benötigt wird ein schönes quadratisches Cover, 2400x2400 mindestens 72dpi für ein Hörbuchcover.
Auf dem Cover soll eine gelb/orange Rose zu in Form einer Blüte zu sehen sein.
Titel: Innere Wandlung
Untertitel: Emotionen sind der Schlüssel für Gesundheit, Energie & Lebensfreude
Autorenname: Dr. med. Birgit Wolkenstein
Das Feloria Logo soll unten mittig sitzen.
Es folgen weiterer Hörbücher von dieser Autorin und es wäre gut wenn man die folgenden Cover in einem ähnlichen Stil halten könnte. Ein harmonisches und gut zu erkennendes Design mit hohem Wiedererkennungseffekt. Ich freue mich auf kreative Designvorschläge.
Auf feloria.de kann man sehen wo das Logo sitzen soll.
Herzliche Grüße - Jens

```html
<!DOCTYPE html>
<html lang="de">
<head>
<meta charset="utf-8">
<title>Innere Wandlung – Hörbuchcover</title>
<link href="https://fonts.googleapis.com/css2?family=Josefin+Sans:wght@300;400;600&family=Yellowtail&display=swap" rel="stylesheet">
<style>
  :root {
    --salmon: #f4937a;
    --ink: #111111;
    --cream: #fdf8ea;
    --peach: #f8c2a0;
    --peach-deep: #f3a070;
    --orange: #ee8a48;
    --petal-light: #fbd9c2;
    --leaf: #c5dc6e;
    --leaf-deep: #6f9a3e;
  }
  html, body {
    margin: 0;
    padding: 0;
    width: 1200px;
    height: 1200px;
    overflow: hidden;
    background: var(--cream);
  }
  .cover {
    position: relative;
    width: 1200px;
    height: 1200px;
    overflow: hidden;
  }
  .garden {
    position: absolute;
    inset: 0;
    background:
      radial-gradient(circle at 640px 560px, rgba(255,253,246,0.96) 0, rgba(255,252,240,0.8) 230px, rgba(255,250,235,0) 420px),
      radial-gradient(circle at 990px 480px, rgba(249,196,150,0.9) 0, rgba(250,214,178,0.6) 45px, rgba(250,222,190,0) 90px),
      radial-gradient(circle at 1010px 820px, rgba(250,208,140,0.9) 0, rgba(251,224,180,0.6) 90px, rgba(251,224,180,0) 150px),
      radial-gradient(circle at 1040px 1060px, rgba(248,196,160,0.9) 0, rgba(250,214,190,0.6) 100px, rgba(250,214,190,0) 170px),
      radial-gradient(circle at 1180px 700px, rgba(250,216,160,0.8) 0, rgba(250,216,160,0) 100px),
      radial-gradient(circle at 440px 230px, rgba(250,206,150,0.85) 0, rgba(250,220,180,0.5) 110px, rgba(250,220,180,0) 200px),
      radial-gradient(circle at 640px 1130px, rgba(242,160,70,0.85) 0, rgba(245,190,120,0.5) 90px, rgba(245,190,120,0) 160px),
      radial-gradient(circle at 40px 200px, var(--leaf) 0, rgba(197,220,110,0) 260px),
      radial-gradient(circle at 60px 1160px, var(--leaf-deep) 0, rgba(111,154,62,0) 240px),
      radial-gradient(circle at 1000px 650px, rgba(200,218,140,0.7) 0, rgba(200,218,140,0) 180px),
      linear-gradient(135deg, #d9e4a0 0%, #fbf6e4 40%, #f8ecd2 100%);
  }
  .main-rose {
    position: absolute;
    left: -120px;
    top: 280px;
    width: 700px;
    height: 700px;
    border-radius: 50%;
    background:
      radial-gradient(circle at 46% 48%, #fbe0cf 0, #f8c4a6 50px, var(--peach-deep) 120px, var(--orange) 170px, var(--peach) 240px, var(--petal-light) 320px, rgba(251,217,194,0) 350px);
  }
  .author {
    position: absolute;
    top: 104px;
    left: 0;
    width: 100%;
    margin: 0;
    text-align: center;
    font-family: "Josefin Sans", sans-serif;
    font-weight: 400;
    font-size: 30px;
    letter-spacing: 1px;
    color: var(--salmon);
  }
  .title-main {
    position: absolute;
    top: 470px;
    left: 0;
    width: 100%;
    margin: 0;
    text-align: center;
    font-family: "Josefin Sans", sans-serif;
    font-weight: 400;
    font-size: 76px;
    letter-spacing: 20px;
    padding-left: 20px;
    box-sizing: border-box;
    color: var(--salmon);
    line-height: 1;
  }
  .title-script {
    position: absolute;
    top: 540px;
    left: 0;
    width: 100%;
    margin: 0;
    text-align: center;
    font-family: "Yellowtail", cursive;
    font-size: 150px;
    color: var(--salmon);
    line-height: 1;
  }
  .subtitle {
    position: absolute;
    top: 760px;
    left: 300px;
    width: 600px;
    margin: 0;
    text-align: center;
    font-family: "Josefin Sans", sans-serif;
    font-weight: 400;
    font-size: 26px;
    line-height: 1.35;
    color: var(--salmon);
  }
  .publisher {
    position: absolute;
    top: 1052px;
    left: 0;
    width: 100%;
    margin: 0;
    text-align: center;
    font-family: "Josefin Sans", sans-serif;
    font-weight: 600;
    font-size: 40px;
    letter-spacing: 5px;
    color: var(--ink);
  }
</style>
</head>
<body>
  <main class="cover">
    <div class="garden" role="img" aria-label="Weichgezeichnetes Foto heller gelb-oranger Rosen vor grünem Hintergrund"></div>
    <div class="main-rose" role="img" aria-label="Große pfirsich-orange Rosenblüte am linken Rand"></div>
    <p class="author">Dr. med. Birgit Wolkenstein</p>
    <h1 class="title-main">INNERE</h1>
    <p class="title-script">wandlung</p>
    <p class="subtitle">Emotionen sind der Schlüssel für Gesundheit, Energie &amp; Lebensfreude</p>
    <p class="publisher">FELORIA</p>
  </main>
</body>
</html>
```